Web Design Project

We have a website in beta that needs updating and are looking for a freash new look for the Home page including Logo.
Our company is called " Pim Sa Ox " we specialize in classified advertising using video. Our consumers will be businesses selling a product or service. Please visit www.pimsaox.com
Our aim past this point is to engage a developer to write the code based on the best design. Our target market is the U.S and I have included some of the landing pages to give you a better idea of what we are trying to acheive

http://www.pimsaox.com/
http://www.pimsaox.com/cars_home.php
http://www.pimsaox.com/boats.php
http://www.pimsaox.com/electronic.php
http://www.pimsaox.com/realestate.php
http://www.pimsaox.com/roommates.php

Target Market(s)

20-35 yr old people who are connected to the internet via mobile phone and use social media on a daily/weekly basis

Industry/Entity Type

Advertising

Requirements
Must have
• We would like to use lots of images to convey it is a video driven website business
Nice to have
• Logo to incorporate same theme of website ( ie ) you are here to watch videos of thinhs to buy & sell
Should not have
• This is to be a freash new site with large type and bold fonts

```html
<!DOCTYPE html>
<html lang="en">
<head>
<meta charset="utf-8">
<title>Pim Sa Ox – Video Classifieds</title>
<link href="https://fonts.googleapis.com/css2?family=Titillium+Web:wght@400;600;700&family=Open+Sans:wght@400;600&display=swap" rel="stylesheet">
<style>
:root{
  --navy:#0b1f5c;
  --navy-deep:#061646;
  --blue-glow:#2a5fc0;
  --search:#1c8fe6;
  --yellow:#f4e64a;
  --red:#d83a1c;
  --red-dark:#b92c10;
  --card:#ececec;
  --line:#dcdcdc;
  --text:#222;
  --muted:#8a8a8a;
  --white:#fff;
}
*{margin:0;padding:0;box-sizing:border-box}
html,body{width:799px;height:1200px;overflow:hidden;background:var(--white)}
body{position:relative;font-family:"Open Sans",Arial,sans-serif;color:var(--text)}
.abs{position:absolute}

/* header */
.hero{left:0;top:0;width:799px;height:383px;
  background:radial-gradient(ellipse at 60% 35%,var(--blue-glow) 0%,#143a93 35%,var(--navy) 70%,var(--navy-deep) 100%)}
.brand{left:95px;top:12px;color:var(--white);font-family:"Titillium Web",sans-serif}
.brand-name{display:flex;align-items:center;gap:6px;font-size:28px;font-weight:700;line-height:30px}
.brand-dot{width:22px;height:22px;border-radius:50%;background:var(--red)}
.brand-tag{font-size:10px;font-weight:600;margin-top:6px;line-height:11px}
.brand-sub{font-size:15px;font-weight:700;line-height:16px}
.top-links{left:410px;top:19px;font-family:"Titillium Web",sans-serif;font-size:10px;font-weight:600;color:var(--yellow);letter-spacing:.3px}
.top-links span{margin:0 4px;color:var(--yellow)}
.search{left:536px;top:16px;width:169px;height:20px;background:var(--search);border-radius:3px;color:var(--white);font-size:8px;line-height:20px;padding-left:7px}
.search svg{position:absolute;right:7px;top:4px}
.nav-btn{top:56px;height:20px;border-radius:3px;background:linear-gradient(#fdfdfd,#cfcfcf);font-family:"Titillium Web",sans-serif;font-size:11px;font-weight:700;color:#222;text-align:center;line-height:20px}
.lang{left:600px;top:56px;width:105px;height:20px;background:var(--white);border-radius:2px;font-size:8px;color:#999;line-height:20px;padding-left:5px}
.lang svg{position:absolute;right:6px;top:8px}
.step{width:146px;height:146px;border-radius:50%;border:5px solid var(--white);box-shadow:0 4px 10px rgba(0,0,0,.4)}
.step-cap{top:315px;width:220px;text-align:center;font-family:"Titillium Web",sans-serif;font-weight:700;font-size:23px;color:var(--white);letter-spacing:.5px}

/* welcome */
.welcome-title{left:94px;top:408px;font-family:"Titillium Web",sans-serif;font-size:15px;font-weight:600}
.welcome-text{left:94px;top:431px;width:456px;font-size:9.3px;line-height:15px;color:var(--muted)}
.welcome-text a{color:var(--red);text-decoration:none}
.feature{top:494px;width:142px;height:162px;background:var(--card);text-align:center}
.feature svg{margin-top:12px}
.feature h3{font-family:"Titillium Web",sans-serif;font-weight:600;font-size:14px;margin-top:6px}
.feature p{font-size:8.5px;line-height:15px;color:#a0a0a0;margin:6px 14px 0}
.btn-more{display:inline-block;margin-top:10px;width:51px;height:19px;border-radius:3px;background:linear-gradient(var(--red),var(--red-dark));color:var(--white);font-size:9.5px;line-height:19px}
.categories{left:564px;top:408px;width:141px;height:248px;background:var(--card)}
.categories h2{height:32px;background:linear-gradient(#e2491f,#c7330f);border-radius:4px 4px 0 0;color:var(--white);font-family:"Titillium Web",sans-serif;font-size:15px;font-weight:600;line-height:32px;padding-left:6px}
.categories li{list-style:none;height:34px;border-bottom:1px solid var(--line);display:flex;align-items:center;gap:9px;padding-left:6px;font-size:11px;color:#333}
.categories li:last-child{border-bottom:none}

/* gallery */
.gallery-title{left:93px;top:683px;font-family:"Titillium Web",sans-serif;font-size:15px;font-weight:600}
.pager{left:673px;top:688px}
.thumb{width:142px;height:132px;border:1px solid #d8d8d8}
.thumb .play{position:absolute;left:55px;top:50px;width:30px;height:30px;border-radius:50%;background:rgba(60,60,60,.7);border:2px solid rgba(255,255,255,.8)}
.thumb .play::after{content:"";position:absolute;left:10px;top:6px;border-left:11px solid var(--white);border-top:7px solid transparent;border-bottom:7px solid transparent}

/* footer */
.footer{left:0;top:1026px;width:799px;height:174px;background:var(--navy)}
.f-col{top:1043px;color:var(--white)}
.f-col h4{font-family:"Titillium Web",sans-serif;font-size:13px;font-weight:600;margin-bottom:9px}
.f-col li{list-style:none;font-size:9px;line-height:17.5px}
.social li{display:flex;align-items:center;gap:8px;height:26px}
.social .sq{width:22px;height:22px;background:var(--white)}
.f-rule{left:94px;top:1170px;width:611px;height:1px;background:rgba(255,255,255,.15)}
.copyright{left:0;top:1179px;width:799px;text-align:center;font-size:8px;color:var(--white)}
</style>
</head>
<body>

<header class="abs hero">
  <div class="abs brand">
    <div class="brand-name">Pim Sa Ox <span class="brand-dot"></span></div>
    <div class="brand-tag">Buy and sell through the</div>
    <div class="brand-sub">#1 Video Classifieds</div>
  </div>
  <div class="abs top-links">CREATE AN ADD <span>|</span> SIGN IN</div>
  <div class="abs search">Enter Your Text...
    <svg width="12" height="12" viewBox="0 0 12 12"><circle cx="5" cy="5" r="3.8" fill="none" stroke="#fff" stroke-width="1.6"/><line x1="8" y1="8" x2="11" y2="11" stroke="#fff" stroke-width="1.8"/></svg>
  </div>
  <div class="abs nav-btn" style="left:286px;width:66px">BUY</div>
  <div class="abs nav-btn" style="left:366px;width:68px">SELL</div>
  <div class="abs nav-btn" style="left:446px;width:66px">INFO</div>
  <div class="abs nav-btn" style="left:526px;width:70px">CONTACT</div>
  <div class="abs lang">Select Language
    <svg width="7" height="5" viewBox="0 0 7 5"><path d="M0 0h7L3.5 5z" fill="#333"/></svg>
  </div>

  <div class="abs step" role="img" aria-label="Video camera recording a product" style="left:108px;top:137px;background:radial-gradient(#f4f4f4,#b9b9b9)"></div>
  <div class="abs step" role="img" aria-label="Keyboard with yellow upload key" style="left:327px;top:137px;background:radial-gradient(#f3cf2a 0%,#6a6a6a 55%,#2c2c2c 100%)"></div>
  <div class="abs step" role="img" aria-label="Seller holding cash next to a speaker" style="left:545px;top:137px;background:radial-gradient(#e8e8e8,#8a9bb5)"></div>
  <svg class="abs" style="left:250px;top:170px" width="300" height="40" viewBox="0 0 300 40">
    <path d="M8 22 Q40 2 72 18" fill="none" stroke="#fff" stroke-width="2"/><path d="M72 18 l-9 -2 l5 -6z" fill="#fff"/>
    <path d="M226 22 Q258 2 290 18" fill="none" stroke="#fff" stroke-width="2"/><path d="M290 18 l-9 -2 l5 -6z" fill="#fff"/>
  </svg>
  <div class="abs step-cap" style="left:72px">CREATE A VIDEO</div>
  <div class="abs step-cap" style="left:290px">UPLOAD TO EASY</div>
  <div class="abs step-cap" style="left:508px">SELL TO BUYER</div>
</header>

<main>
  <h1 class="abs welcome-title">WELCOME TO PIM SA OX</h1>
  <p class="abs welcome-text">Lorem Ipsum is simply dummy text of the printing and typesetting industry. Lorem Ipsum has been the industry's standard dummy text ever since the 1500s, when an unknown printer took a galley of type and scrambled it to make a type specimen book. It has survived not only five centuries, but also... <a href="#">Read More</a></p>

  <section class="abs feature" style="left:94px">
    <svg width="28" height="30" viewBox="0 0 28 30"><rect x="1.5" y="1.5" width="25" height="27" fill="none" stroke="#222" stroke-width="2"/><g stroke="#222" stroke-width="2"><line x1="6" y1="9" x2="8" y2="9"/><line x1="11" y1="9" x2="22" y2="9"/><line x1="6" y1="15" x2="8" y2="15"/><line x1="11" y1="15" x2="22" y2="15"/><line x1="6" y1="21" x2="8" y2="21"/><line x1="11" y1="21" x2="22" y2="21"/></g></svg>
    <h3>Most View</h3>
    <p>Lorem Ipsum is simply dummy text of the printing and type...</p>
    <span class="btn-more">More</span>
  </section>
  <section class="abs feature" style="left:251px">
    <svg width="28" height="28" viewBox="0 0 28 28"><rect x="2" y="2" width="24" height="24" rx="3" fill="#333"/><circle cx="14" cy="14" r="7" fill="none" stroke="#fff" stroke-width="1.6"/><path d="M14 10v4h3" fill="none" stroke="#fff" stroke-width="1.6"/></svg>
    <h3 style="margin-top:2px">Most Recent</h3>
    <p>Lorem Ipsum is simply dummy text of the printing and type...</p>
    <span class="btn-more">More</span>
  </section>
  <section class="abs feature" style="left:407px">
    <svg width="28" height="28" viewBox="0 0 28 28"><path d="M9 2l5 6 5-6" fill="none" stroke="#222" stroke-width="2"/><rect x="2" y="8" width="24" height="17" fill="none" stroke="#222" stroke-width="2.4"/></svg>
    <h3 style="margin-top:2px">Most Interesting</h3>
    <p>Lorem Ipsum is simply dummy text of the printing and type...</p>
    <span class="btn-more">More</span>
  </section>

  <aside class="abs categories">
    <h2>Categories</h2>
    <ul>
      <li><svg width="18" height="10" viewBox="0 0 18 10"><path d="M1 8V5l3-3h8l4 3v3z" fill="#222"/><circle cx="5" cy="8" r="2" fill="#222"/><circle cx="13" cy="8" r="2" fill="#222"/></svg>Car</li>
      <li><svg width="18" height="10" viewBox="0 0 18 10"><path d="M1 5h16l-3 5H4z" fill="#222"/><path d="M8 0v5h5z" fill="#222"/></svg>Boat</li>
      <li><svg width="18" height="12" viewBox="0 0 18 12"><rect x="5" y="2" width="8" height="8" fill="none" stroke="#222" stroke-width="1.6"/><g stroke="#222"><line x1="3" y1="4" x2="15" y2="4"/><line x1="3" y1="8" x2="15" y2="8"/></g></svg>Electronics</li>
      <li><svg width="18" height="12" viewBox="0 0 18 12"><path d="M2 6l7-5 7 5v6H2z" fill="#222"/></svg>Real Estate</li>
      <li><svg width="18" height="12" viewBox="0 0 18 12"><circle cx="6" cy="4" r="3" fill="#222"/><circle cx="12" cy="4" r="3" fill="#222"/><path d="M1 12l5-5 5 5M7 12l5-5 5 5" fill="#222"/></svg>Roommate</li>
      <li><svg width="18" height="14" viewBox="0 0 14 14"><rect x="1" y="1" width="12" height="12" fill="none" stroke="#222" stroke-width="1.6"/><rect x="4" y="4" width="2" height="2" fill="#222"/><rect x="8" y="4" width="2" height="2" fill="#222"/><rect x="4" y="8" width="2" height="2" fill="#222"/><rect x="8" y="8" width="2" height="2" fill="#222"/></svg>Other Categories</li>
    </ul>
  </aside>

  <h2 class="abs gallery-title">Our Video Gallery</h2>
  <svg class="abs pager" width="34" height="16" viewBox="0 0 34 16"><path d="M10 1L3 8l7 7" fill="none" stroke="#444" stroke-width="2"/><path d="M24 1l7 7-7 7" fill="none" stroke="#444" stroke-width="2"/></svg>

  <div class="abs thumb" role="img" aria-label="Wooden boat for sale on a beach" style="left:94px;top:711px;background:linear-gradient(#cfd8de 0%,#a9b3b8 45%,#d7c9b4 70%,#9c8a72 100%)"><span class="play"></span></div>
  <div class="abs thumb" role="img" aria-label="Silver car with sale sign" style="left:251px;top:711px;background:radial-gradient(#dcdcdc,#f7f7f7)"><span class="play"></span></div>
  <div class="abs thumb" role="img" aria-label="House with for sale sign" style="left:407px;top:711px;background:linear-gradient(#8fae6e,#b8a99a 50%,#5f7f3f)"><span class="play"></span></div>
  <div class="abs thumb" role="img" aria-label="Young man in a painted t-shirt" style="left:564px;top:711px;background:radial-gradient(#e9e2d2,#c9d8e4)"><span class="play"></span></div>
  <div class="abs thumb" role="img" aria-label="Hand holding a smartphone" style="left:94px;top:857px;background:radial-gradient(#e87a2a 0%,#f0c9a0 45%,#fafafa 70%)"><span class="play"></span></div>
  <div class="abs thumb" role="img" aria-label="Roommates relaxing on a sofa" style="left:251px;top:857px;background:linear-gradient(#7fb8b4,#4c8a8a 60%,#d9d3c4)"><span class="play"></span></div>
  <div class="abs thumb" role="img" aria-label="Kitchen appliances" style="left:407px;top:857px;background:radial-gradient(#d4d6d8,#f8f8f8)"><span class="play"></span></div>
  <div class="abs thumb" role="img" aria-label="Narrowboat on a canal" style="left:564px;top:857px;background:linear-gradient(#7ea05a,#2a3a6a 55%,#5a6a3a)"><span class="play"></span></div>
</main>

<footer class="abs footer"></footer>
<div class="abs f-col" style="left:105px"><h4>BUY/BROWSE</h4><ul><li>Roommates</li><li>Cars</li><li>Boats</li><li>Electronics</li><li>Others</li></ul></div>
<div class="abs f-col" style="left:224px"><h4>SELL</h4><ul><li>Start Selling</li><li>Login</li><li>Shooting Video</li><li>Uploading Video</li><li>Buying</li></ul></div>
<div class="abs f-col" style="left:342px"><h4>INFO</h4><ul><li>VBlog</li><li>FAQ</li><li>Terms of Use</li><li>Privacy Policy</li><li>Buyer/Seller Safety</li></ul></div>
<div class="abs f-col" style="left:461px"><h4>CONTACT</h4><ul><li>Contact Us</li><li>Feedback Form</li><li>Referral Program</li><li>Business Register</li><li>Subscription</li></ul></div>
<div class="abs f-col social" style="left:578px"><h4>FOLLOW WITH US</h4><ul><li><span class="sq"></span>Join Us On Friendwall</li><li><span class="sq"></span>Follow Us On Chirpline</li><li><span class="sq"></span>RSS Feed</li></ul></div>
<div class="abs f-rule"></div>
<div class="abs copyright">2013 © Pim Sa Ox. All Rights Reserved.</div>

</body>
</html>
```